Business Card Design for a Personal Trainer

I need a business card design for my job as a personal trainer. It should have a unique, modern and exclusive design. On the front there should be only my logo with my name and my job. 0163/2918374 Tobias Kellinger Lindenfeldweg 14 80412 Munich Germany The most important contact information is the web adress. it can be bigger than the rest, but its not necessary. The card should be 8,5cmx5,5cm big. Font: Roboto. Colors: black, white, gray, 56c1ff.

```html
<!DOCTYPE html>
<html lang="de">
<head>
<meta charset="utf-8">
<title>Tobias Kellinger – Visitenkarte</title>
<link href="https://fonts.googleapis.com/css2?family=Roboto:wght@400&family=Work+Sans:wght@400;500&display=swap" rel="stylesheet">
<style>
  :root {
    --page: #e0e0e0;
    --paper: #ffffff;
    --ink: #1a1a1a;
    --night: #050505;
    --photo-light: #4a4a4a;
    --photo-dark: #111111;
  }
  * { margin: 0; padding: 0; box-sizing: border-box; }
  html, body { width: 1200px; height: 897px; overflow: hidden; background: var(--page); }
  .canvas { position: relative; width: 1200px; height: 897px; }

  .card { position: absolute; left: 329px; width: 543px; height: 310px; overflow: hidden; }
  .card--front { top: 108px; background: var(--paper); color: var(--ink); }
  .card--back { top: 479px; background: var(--night); color: var(--paper); }

  .brand { position: absolute; display: flex; flex-direction: column; align-items: center; transform: translateX(-50%); }
  .brand__square { width: 40px; height: 40px; background: currentColor; margin-bottom: 30px; }
  .brand__name { font-family: "Roboto", sans-serif; font-weight: 400; font-size: 25px; letter-spacing: 0.2px; white-space: nowrap; line-height: 24px; }
  .brand__tagline { align-self: stretch; display: flex; align-items: center; gap: 4px; margin-top: 4px;
    font-family: "Roboto", sans-serif; font-weight: 400; font-size: 9.5px; letter-spacing: 2.6px; line-height: 11px; white-space: nowrap; }
  .brand__rule { flex: 1; height: 1px; background: currentColor; }
  .card--front .brand { left: 148px; top: 100px; }
  .card--back .brand { left: 399px; top: 95px; }

  .divider { position: absolute; left: 293px; top: 86px; width: 2px; height: 140px; background: var(--ink); }

  .details { position: absolute; left: 324px; top: 82px; font-family: "Work Sans", sans-serif; font-size: 13.5px; line-height: 19px; }
  .details__name { font-weight: 500; font-size: 17px; letter-spacing: 0.6px; text-transform: uppercase; line-height: 20px; }
  .details__role { margin-bottom: 7px; }
  .details__address { margin-bottom: 7px; }
  .contact { list-style: none; }
  .contact li { display: flex; align-items: center; gap: 6px; }
  .contact svg { width: 9px; height: 9px; flex: none; }

  .portrait { position: absolute; left: 0; top: 0; width: 255px; height: 310px;
    background: radial-gradient(ellipse at 50% 55%, var(--photo-light) 0%, var(--photo-dark) 70%, var(--night) 100%); }
</style>
</head>
<body>
<main class="canvas">
  <section class="card card--front" aria-label="Vorderseite">
    <div class="brand">
      <span class="brand__square"></span>
      <span class="brand__name">TOBIAS KELLINGER</span>
      <span class="brand__tagline"><span class="brand__rule"></span>PERSONAL TRAINER<span class="brand__rule"></span></span>
    </div>
    <div class="divider"></div>
    <div class="details">
      <p class="details__name">Tobias Kellinger</p>
      <p class="details__role">Personal Trainer</p>
      <p class="details__address">Lindenfeldweg 14<br>80412 München</p>
      <ul class="contact">
        <li><svg viewBox="0 0 10 10"><path d="M2.5 0.8 L4 3 L3 4 Q4 6.2 6 7 L7 6 L9.2 7.5 L8 9.2 Q3.5 9 0.8 2 Z" fill="currentColor"/></svg>0163/2918374</li>
        <li><svg viewBox="0 0 10 10"><rect x="0.8" y="2" width="8.4" height="6" fill="none" stroke="currentColor" stroke-width="1"/><path d="M0.8 2 L5 5.5 L9.2 2" fill="none" stroke="currentColor" stroke-width="1"/></svg>t.kellinger@mailbox.de</li>
        <li><svg viewBox="0 0 10 10"><circle cx="5" cy="5" r="4.2" fill="none" stroke="currentColor" stroke-width="1"/><ellipse cx="5" cy="5" rx="1.8" ry="4.2" fill="none" stroke="currentColor" stroke-width="0.8"/><path d="M0.8 5 H9.2" stroke="currentColor" stroke-width="0.8"/></svg>www.tobiaskellinger.de</li>
      </ul>
    </div>
  </section>

  <section class="card card--back" aria-label="Rückseite">
    <div class="portrait" role="img" aria-label="Schwarz-weiß Porträtfoto des Trainers mit verschränkten Armen vor schwarzem Hintergrund"></div>
    <div class="brand">
      <span class="brand__square"></span>
      <span class="brand__name">TOBIAS KELLINGER</span>
      <span class="brand__tagline"><span class="brand__rule"></span>PERSONAL TRAINER<span class="brand__rule"></span></span>
    </div>
  </section>
</main>
</body>
</html>
```